Two Separate Canvas Posters 54"width x 36" Height

I need two (2) posters designed for a new restaurant concept called: Lumaro Fresh Pita Grill.
Both posters will be printed on Canvas and placed into our new restaurants dining area.
I want this to look hip and cool.
I want so see red colors and earth tones. Please see attached for some ideas that I have.
The final design should communicate that you really gotta have this product and that this is a fun and casual place for a quick bite on the go.
Poster 1 message: gotta Eatta pita!
Size: 54"width x 36" high
Idea: Please see attached for design ideas and colors that I would like to see. If you can come up with any better idea, I would love to see this.
Poster 2 message: Power to the Pita
Size: 54"width x 36" height
Idea: Please see attached for design idea and colors that I want to see.
Restaurant

```html
<!DOCTYPE html>
<html lang="en">
<head>
<meta charset="utf-8">
<title>Gotta Eatta Pita!</title>
<link rel="stylesheet" href="https://fonts.googleapis.com/css2?family=Oswald:wght@700&display=swap">
<style>
  :root {
    --ground-red: #8a0c06;
    --ground-deep: #5e0803;
    --pattern-rust: #7c3410;
    --type-orange: #e0862a;
    --type-mustard: #d2a914;
  }
  html, body {
    margin: 0;
    padding: 0;
    width: 1200px;
    height: 800px;
    overflow: hidden;
    background: var(--ground-red);
  }
  .poster {
    display: block;
    width: 1200px;
    height: 800px;
  }
  .headline {
    font-family: "Oswald", "Arial Narrow", sans-serif;
    font-weight: 700;
  }
  .headline--gotta { fill: var(--type-mustard); }
  .headline--eatta { fill: var(--type-orange); }
  .headline--pita  { fill: var(--type-mustard); }
</style>
</head>
<body>
<svg class="poster" viewBox="0 0 1200 800" xmlns="http://www.w3.org/2000/svg">
  <defs>
    <radialGradient id="ground-tone" cx="50%" cy="50%" r="70%">
      <stop offset="0%" stop-color="#8a240a"/>
      <stop offset="55%" stop-color="var(--pattern-rust)"/>
      <stop offset="100%" stop-color="var(--ground-deep)"/>
    </radialGradient>
    <radialGradient id="edge-shade" cx="50%" cy="50%" r="75%">
      <stop offset="70%" stop-color="#000" stop-opacity="0"/>
      <stop offset="100%" stop-color="#2a0400" stop-opacity="0.55"/>
    </radialGradient>
  </defs>

  <rect class="ground" width="1200" height="800" fill="var(--ground-red)"/>
  <rect class="ground-pattern" width="1200" height="800" fill="url(#ground-tone)" opacity="0.6"
        role="img" aria-label="Cracked, weathered pattern of overlapping rust-brown rings on deep red"/>
  <rect class="ground-edge" width="1200" height="800" fill="url(#edge-shade)"/>

  <g class="headline-group">
    <text class="headline headline--gotta" transform="translate(233 795) rotate(-90)"
          font-size="253" textLength="790" lengthAdjust="spacingAndGlyphs">GOTTA</text>
    <text class="headline headline--eatta" x="260" y="386"
          font-size="476" textLength="915" lengthAdjust="spacingAndGlyphs">EATTA</text>
    <text class="headline headline--pita" x="258" y="790"
          font-size="490" textLength="912" lengthAdjust="spacingAndGlyphs">PITA!</text>
  </g>
</svg>
</body>
</html>
```